Business Name is TL Glamworks - Make-up Artist

I'm looking for an attractive and eye catching business card for for mobile make-up artist business. On the front of the card, I just want the name TL Glamworks in feminine type cursive writing and underneath my name Tessa Lowrie and Make-Up Artist.
On the back of the card, I would like written down one side the following;
Make-Up Tutorials
Bridal
Photography
Debutante
Formals
Family Portraits
I would also like the following details as well as the Chatterbook and Snapgram Icons;
Mobile: 0462 318 725
Email: tessalowrie@mailbox-demo.com
Website: tessalowrie.velmora-demo.com
Certificate III in Make-Up
Also, I would like a section that says Your Next Appointment and a space to put that information.
I would also like the Velmora Symbol on the bottom right hand corner (I have attached)

Target Market(s)

Mostly females

Industry/Entity Type

Makeup

Contact Information for Business Card

TL Glamworks
Tessa Lowrie - Make-Up Artist

Font styles to use
Script

Colors
b768aa
886aae
e34297

Requirements
Must have
• Mobile: 0462 318 725
• Email: tessalowrie@mailbox-demo.com
• Website: tessalowrie.velmora-demo.com
• Certificate III in Make-Up
Nice to have
• Something to do with make-up like a smudged lipstick or some eye shadow
Should not have
• Don't want it too busy

```html
<!DOCTYPE html>
<html lang="en">
<head>
<meta charset="utf-8">
<title>TL Glamworks – Business Card</title>
<link rel="stylesheet" href="https://fonts.googleapis.com/css2?family=Montserrat:wght@300;400;600;700&family=Dancing+Script:wght@600&display=swap">
<style>
  :root {
    --page: #ece9e6;
    --card: #ffffff;
    --ink: #1d1d1f;
    --ink-soft: #3a3a3c;
    --panel: #dedede;
    --rule: #2b2b2b;
    --orchid: #b768aa;
    --lavender: #886aae;
    --magenta: #e34297;
    --partner: #1f7a2e;
    --font: "Montserrat", Arial, sans-serif;
    --script: "Dancing Script", cursive;
  }
  * { box-sizing: border-box; margin: 0; padding: 0; }
  html, body { width: 1200px; height: 800px; overflow: hidden; }
  body {
    background: var(--page);
    font-family: var(--font);
    color: var(--ink);
    position: relative;
  }
  .card {
    position: absolute;
    top: 241px;
    width: 520px;
    height: 318px;
    background: var(--card);
    box-shadow: 0 6px 18px rgba(0,0,0,0.12);
  }
  .card--back { left: 50px; }
  .card--front { left: 630px; }

  /* Back */
  .social-row {
    position: absolute; left: 30px; right: 30px; top: 28px; height: 20px;
    display: flex; align-items: center; gap: 12px;
  }
  .social-row__rule { flex: 1; height: 1.5px; background: var(--rule); }
  .social { display: flex; gap: 14px; align-items: center; white-space: nowrap; }
  .social__item { display: flex; align-items: center; gap: 5px; font-size: 9px; font-weight: 600; }
  .social__dot { width: 12px; height: 12px; border-radius: 50%; background: var(--ink); }

  .rule { position: absolute; height: 1.5px; background: var(--rule); }
  .rule--appointment { left: 250px; right: 30px; top: 262px; }
  .rule--bottom { left: 30px; right: 30px; top: 296px; }

  .panel {
    position: absolute; left: 30px; right: 30px; top: 58px; height: 182px;
    background: var(--panel);
    border-radius: 0 40px 0 40px;
    display: flex; align-items: center;
  }
  .contact {
    flex: 1; text-align: center; font-size: 12.5px; line-height: 1.45; color: var(--ink-soft);
    padding-top: 50px;
  }
  .contact__cert { font-weight: 700; color: var(--ink); }
  .panel__divider { width: 1.5px; height: 110px; background: var(--rule); }
  .services {
    flex: 1; text-align: center; font-size: 12.5px; line-height: 1.45; color: var(--ink-soft);
    padding-bottom: 40px;
  }
  .services__sep { margin: 0 6px; }

  .appointment {
    position: absolute; left: 30px; top: 254px;
    font-size: 11px; font-weight: 600; letter-spacing: 0.3px; text-transform: uppercase;
  }
  .partner {
    position: absolute; right: 44px; top: 206px;
    display: flex; align-items: center; gap: 4px;
    font-size: 10px; font-weight: 600; color: var(--partner); white-space: nowrap;
  }
  .partner__dot { width: 9px; height: 9px; border-radius: 50%; background: var(--partner); }

  /* Front */
  .brand {
    position: absolute; left: 0; right: 0; top: 92px;
    display: flex; justify-content: center; align-items: center; gap: 14px;
  }
  .brand__circle {
    width: 46px; height: 46px; border-radius: 50%; background: var(--magenta);
  }
  .brand__name {
    font-family: var(--script); font-size: 44px; font-weight: 600;
    color: var(--lavender); line-height: 1.2; white-space: nowrap;
  }
  .identity {
    position: absolute; left: 0; right: 0; top: 232px;
    display: flex; justify-content: center; align-items: baseline; gap: 16px;
  }
  .identity__name { font-size: 19px; font-weight: 700; }
  .identity__role { font-size: 19px; font-weight: 300; color: var(--ink-soft); }
</style>
</head>
<body>
  <section class="card card--back" aria-label="Back of business card">
    <div class="social-row">
      <span class="social-row__rule"></span>
      <div class="social">
        <span class="social__item"><span class="social__dot"></span>Snapgram</span>
        <span class="social__item"><span class="social__dot"></span>Chatterbook</span>
      </div>
      <span class="social-row__rule"></span>
    </div>

    <div class="panel">
      <div class="contact">
        <p>0462 318 725</p>
        <p>tessalowrie@mailbox-demo.com</p>
        <p>tessalowrie.velmora-demo.com</p>
        <p class="contact__cert">Certificate III in Make-Up</p>
      </div>
      <div class="panel__divider"></div>
      <div class="services">
        <p>Make-Up Tutorials</p>
        <p>Bridal<span class="services__sep">|</span>Photography</p>
        <p>Debutante<span class="services__sep">|</span>Formals</p>
        <p>Family Portraits</p>
      </div>
    </div>

    <div class="partner"><span class="partner__dot"></span>Velmora</div>

    <p class="appointment">Your Next Appointment</p>
    <div class="rule rule--appointment"></div>
    <div class="rule rule--bottom"></div>
  </section>

  <section class="card card--front" aria-label="Front of business card">
    <div class="brand">
      <span class="brand__circle"></span>
      <span class="brand__name">TL Glamworks</span>
    </div>
    <div class="identity">
      <span class="identity__name">Tessa Lowrie</span>
      <span class="identity__role">Make-Up Artist</span>
    </div>
  </section>
</body>
</html>
```